LPS AUDITION

I need a post card design (front only) with this on it:
Leap Pulse Stride (this is the main title to be in all caps)
Auditions
Date: Thursday June 30th
6:30-8:30 PM in person
Address: 4172 Kestrel BLVD, Oakland CA 94605
video submissions turn in by Sunday July 3rd, 2022 email:LeapPulseStride22@movenote.test
Teens and Adults welcomed

SO PLEASE COME UP WITH A DESIGN THATS COLORFUL AND INVITING THX!

```html
<!DOCTYPE html>
<html lang="en">
<head>
<meta charset="utf-8">
<title>Leap Pulse Stride Auditions Postcard</title>
<link rel="stylesheet" href="https://fonts.googleapis.com/css2?family=Montserrat:wght@400;600;700;800&family=Oswald:wght@500;600&display=swap">
<style>
  :root {
    --page-bg: #e0dcdb;
    --card-bg: #07060f;
    --magenta: #ff1fb4;
    --magenta-soft: #f040c8;
    --cyan: #10d2ff;
    --violet: #7a4cf0;
    --white: #ffffff;
  }
  * { margin: 0; padding: 0; box-sizing: border-box; }
  html, body { width: 1200px; height: 1200px; overflow: hidden; }
  body { background: var(--page-bg); position: relative; font-family: "Montserrat", sans-serif; }

  .postcard {
    position: absolute; left: 20px; top: 214px; width: 1160px; height: 772px;
    overflow: hidden;
    background:
      radial-gradient(ellipse 55% 70% at 85% 45%, rgba(140, 20, 150, 0.55), transparent 70%),
      radial-gradient(ellipse 40% 50% at 60% 20%, rgba(200, 30, 120, 0.35), transparent 70%),
      linear-gradient(180deg, #07060f 0%, #0b0a1c 55%, #0c1530 85%, #0a0f22 100%);
  }
  .dancer-photo {
    position: absolute; left: 560px; top: 70px; width: 560px; height: 680px;
    border-radius: 40% 45% 35% 40%;
    background: radial-gradient(ellipse at 50% 45%, rgba(120, 60, 170, 0.55), rgba(80, 20, 110, 0.3) 55%, transparent 75%);
  }
  .presenter {
    position: absolute; left: 50px; top: 52px;
    color: var(--magenta-soft); font-weight: 400; font-size: 23px; line-height: 32px; letter-spacing: 0.5px;
  }
  .title {
    position: absolute; left: 48px; top: 114px;
    font-weight: 700; font-size: 122px; line-height: 100px; letter-spacing: -1px;
  }
  .title span { display: block; }
  .title .line-leap { color: var(--magenta); }
  .title .line-pulse {
    background: linear-gradient(90deg, var(--cyan), var(--violet) 55%, var(--magenta));
    -webkit-background-clip: text; background-clip: text; color: transparent;
  }
  .title .line-stride { color: var(--cyan); }
  .title-rule {
    position: absolute; left: 52px; top: 434px; width: 450px; height: 3px;
    background: linear-gradient(90deg, #fff, rgba(255,255,255,0.6));
  }
  .subtitle {
    position: absolute; left: 50px; top: 448px;
    color: var(--white); font-weight: 600; font-size: 48px; letter-spacing: 24px;
  }
  .date-day {
    position: absolute; left: 52px; top: 510px;
    font-family: "Oswald", sans-serif; font-weight: 600; font-size: 84px; line-height: 92px; color: var(--white);
    white-space: nowrap;
  }
  .date-day .num { color: var(--magenta); }
  .date-day sup { font-size: 44px; vertical-align: 32px; color: var(--magenta); margin-right: 8px; }
  .date-weekday {
    position: absolute; left: 55px; top: 606px;
    color: var(--white); font-weight: 700; font-size: 40px; letter-spacing: 0.5px;
  }
  .date-divider { position: absolute; left: 372px; top: 522px; width: 2px; height: 102px; background: var(--white); }
  .details { position: absolute; left: 394px; top: 518px; color: var(--white); font-weight: 700; }
  .details .time { color: var(--magenta-soft); font-size: 24px; line-height: 30px; letter-spacing: 0.5px; }
  .detail-row { display: flex; align-items: flex-start; gap: 14px; margin-top: 8px; font-size: 17px; line-height: 23px; letter-spacing: 0.4px; white-space: nowrap; }
  .detail-row svg { flex: none; margin-top: 2px; }
  .submission {
    position: absolute; left: 50px; top: 653px; display: flex; align-items: center; gap: 10px;
    color: var(--white); font-weight: 700; font-size: 20px; white-space: nowrap;
  }
  .submission .deadline { background: var(--magenta); padding: 5px 10px; font-size: 22px; }
  .welcome {
    position: absolute; left: 50px; top: 700px;
    color: var(--cyan); font-weight: 800; font-size: 35px; letter-spacing: 0.8px; white-space: nowrap;
  }
</style>
</head>
<body>
  <main class="postcard">
    <div class="dancer-photo" role="img" aria-label="Photo of a hooded street dancer leaping mid-air, wrapped in glowing magenta light rings"></div>

    <p class="presenter">BRIGHTSTEP PRODUCTIONS PRESENTS<br>MAYA CORBIN'S</p>

    <h1 class="title">
      <span class="line-leap">LEAP</span>
      <span class="line-pulse">PULSE</span>
      <span class="line-stride">STRIDE</span>
    </h1>
    <div class="title-rule"></div>
    <h2 class="subtitle">AUDITIONS</h2>

    <p class="date-day"><span class="num">30</span><sup>TH</sup>JUNE</p>
    <p class="date-weekday">THURSDAY</p>
    <div class="date-divider"></div>

    <div class="details">
      <p class="time">6:30-8:30 PM in person</p>
      <div class="detail-row">
        <svg width="20" height="24" viewBox="0 0 20 24" aria-hidden="true">
          <path d="M10 1a7 7 0 0 0-7 7c0 5 7 11 7 11s7-6 7-11a7 7 0 0 0-7-7z" fill="none" stroke="#ff1fb4" stroke-width="2.5"/>
          <circle cx="10" cy="8" r="2.5" fill="#ff1fb4"/>
          <ellipse cx="10" cy="21.5" rx="7" ry="1.6" fill="none" stroke="#ff1fb4" stroke-width="1.6"/>
        </svg>
        <span>4172 Kestrel BLVD, Oakland<br>CA 94605</span>
      </div>
      <div class="detail-row">
        <svg width="22" height="16" viewBox="0 0 22 16" aria-hidden="true">
          <rect x="0" y="1" width="22" height="14" fill="#ff1fb4"/>
          <path d="M1 2l10 7 10-7" fill="none" stroke="#07060f" stroke-width="1.8"/>
        </svg>
        <span>LeapPulseStride22@movenote.test</span>
      </div>
    </div>

    <p class="submission">Video submissions turn in by <span class="deadline">Sunday July 3rd, 2022</span></p>
    <p class="welcome">TEENS AND ADULTS WELCOMED</p>
  </main>
</body>
</html>
```